Redesign responsive website and logo for webshop platform

Redesign our applications old website with a new clean, crisp modern looking style that is responsive.

Our application is a cloud based, free ecommerce platform that lets users set up their own webshops within minutes. (Similar to Bramvik https://bramvik.example/l/sell)

Our old website: http://sv.kelporia.example/

I need redesigned HTML + CSS for the following three pages:
* Landing Page:
(Old page: http://sv.kelporia.example/)
I have attached a mockup of a proposed layout/structure for the landing page.
- Pricing comparision/features page
(Old page http://sv.kelporia.example/t/funktioner)
- Generic "article" page:
(Old page http://sv.kelporia.example/d/redigerasida)

The pages must responsive using HTML 5/CSS 3 (I prefer Bootstrap 3 if possible).

I also need a redesign of the logotype.

If you have any questions don't hesitate to ask and we will provide whatever is needed to you.

Logo Text

Kelporia

Coding

Coded - Design and coding required

Number of Pages Required

3 page

Font styles to use
Serif
Sans Serif

```html
<!DOCTYPE html>
<html lang="en">
<head>
<meta charset="utf-8">
<title>Kelporia – Welcome</title>
<link href="https://fonts.googleapis.com/css2?family=Lato:wght@400;700&family=Roboto:wght@300;400;500;700&display=swap" rel="stylesheet">
<style>
:root{
  --blue:#1e9ad6;
  --royal:#1f63b8;
  --royal-dark:#184f96;
  --ink:#262626;
  --card-dark:#2b2b2b;
  --muted:#8a8a8a;
  --panel:#ececec;
  --white:#ffffff;
  --heading:#222222;
}
*{box-sizing:border-box;margin:0;padding:0}
html,body{width:680px;height:1200px;overflow:hidden}
body{position:relative;background:var(--white);font-family:'Roboto',sans-serif;color:var(--ink)}
.abs{position:absolute}

/* hero */
.hero{position:absolute;left:0;top:0;width:680px;height:354px;overflow:hidden}
.hero-photo{position:absolute;inset:0;background:
  radial-gradient(ellipse at 72% 30%,rgba(196,160,120,.75),rgba(0,0,0,0) 55%),
  radial-gradient(ellipse at 20% 80%,rgba(120,90,60,.5),rgba(0,0,0,0) 50%),
  linear-gradient(100deg,#1b1f24 0%,#2a2b2d 40%,#574a3c 70%,#3b352f 100%)}
.hero-shade{position:absolute;inset:0;background:rgba(10,12,16,.35)}
.brand{font-family:'Roboto',sans-serif;font-weight:700;color:var(--white);font-size:17px;letter-spacing:.3px;text-transform:uppercase}
.topbar-line{left:56px;top:56px;width:568px;height:1px;background:rgba(255,255,255,.45)}
.btn-login{left:396px;top:21px;width:55px;height:22px;background:var(--blue);color:var(--white);font-size:10px;font-weight:500;display:flex;align-items:center;justify-content:center;border-radius:2px}
.social{display:flex;gap:4px}
.social span{width:19px;height:19px;border:1.5px solid var(--white);border-radius:50%;display:block}
.menu-btn{left:592px;top:18px;width:32px;height:27px;border:1.5px solid var(--white);border-radius:2px;display:flex;align-items:center;justify-content:center}
.hero-title{left:0;width:680px;top:100px;text-align:center;font-family:'Lato',sans-serif;font-weight:700;font-size:29px;color:var(--white)}
.hero-lead{left:115px;width:450px;top:151px;text-align:center;font-size:8.6px;line-height:17.5px;color:var(--white)}
.signup{left:85px;top:210px;width:510px;height:51px;border:1px solid rgba(255,255,255,.7);border-radius:3px;background:rgba(0,0,0,.35)}
.field{top:224px;width:155px;height:24px;background:var(--white);border-radius:2px;font-size:7.5px;color:#333;padding-left:6px;display:flex;align-items:center}
.btn-create{left:428px;top:224px;width:155px;height:24px;background:var(--royal);border:1px solid #6fa3e6;border-radius:2px;color:var(--white);font-size:8.5px;font-weight:500;display:flex;align-items:center;justify-content:center}

/* service cards */
.card{position:absolute;width:279px;height:116px;border-left:3px solid var(--blue);color:var(--white)}
.card.sky{background:linear-gradient(135deg,#2aa3dc,#1a8fcb)}
.card.night{background:linear-gradient(135deg,#333,#252525)}
.card.royal{background:linear-gradient(135deg,#2468be,#1d5aaa);border-left-color:var(--royal-dark)}
.card svg{position:absolute;left:15px;top:28px}
.card h3{position:absolute;left:77px;top:20px;font-size:12.6px;font-weight:500;text-transform:uppercase;letter-spacing:.1px}
.card p{position:absolute;left:78px;top:45px;width:186px;font-size:7.6px;line-height:13.6px;text-align:justify}

/* features */
.features{position:absolute;left:0;top:786px;width:680px;height:230px;background:var(--panel)}
.features-title{position:absolute;left:0;width:680px;top:18px;text-align:center;font-size:19px;font-weight:400;color:var(--heading)}
.features-title em{font-style:normal;color:var(--blue)}
.features-rule{position:absolute;left:311px;top:48px;width:58px;height:1px;background:#333}
.feature{position:absolute;width:180px}
.feature svg{position:absolute;left:0;top:0}
.feature h4{position:absolute;left:40px;top:0;font-size:11px;font-weight:400;color:var(--heading);white-space:nowrap}
.feature p{position:absolute;left:40px;top:18px;width:140px;font-size:7px;line-height:12.6px;color:var(--muted);font-weight:300}

/* footer */
.footer{position:absolute;left:0;top:1016px;width:680px;height:184px;background:linear-gradient(135deg,#2166bb,#1c5cae);color:var(--white)}
.footer .brand{position:absolute;left:0;width:680px;top:24px;text-align:center;font-size:20px}
.contact{position:absolute;top:66px;display:flex;align-items:center;gap:7px;font-size:10.5px}
.contact i{width:18px;height:18px;border:1.3px solid var(--white);border-radius:50%;display:flex;align-items:center;justify-content:center}
.footer-nav{position:absolute;left:0;width:680px;top:106px;display:flex;justify-content:center;gap:14px;font-size:9.6px;font-weight:500;text-transform:uppercase}
.footer-nav .sep{font-weight:300}
.footer-line{position:absolute;left:56px;top:138px;width:568px;height:1px;background:rgba(255,255,255,.6)}
.copyright{position:absolute;left:56px;top:154px;font-size:8px}
.footer .social{position:absolute;left:516px;top:151px}
</style>
</head>
<body>

<header class="hero">
  <div class="hero-photo" role="img" aria-label="Photo of a smiling woman using a smartphone in a café"></div>
  <div class="hero-shade"></div>
  <div class="abs brand" style="left:56px;top:22px">Kelporia</div>
  <div class="abs btn-login">LOGIN</div>
  <div class="abs social" style="left:462px;top:22px"><span></span><span></span><span></span><span></span><span></span></div>
  <div class="abs menu-btn">
    <svg width="12" height="10" viewBox="0 0 12 10"><rect y="0" width="12" height="2" fill="#fff"/><rect y="4" width="12" height="2" fill="#fff"/><rect y="8" width="12" height="2" fill="#fff"/></svg>
  </div>
  <div class="abs topbar-line"></div>
  <h1 class="abs hero-title">Welcome To Kelporia</h1>
  <p class="abs hero-lead">Kelporia är en tjänst som låter dig starta en komplett internetbutik. Tjänsten är gratis och har allt som krävs för att du ska komma igång med din verksamhet och sälja produkter online.</p>
  <div class="abs signup"></div>
  <div class="abs field" style="left:98px">Name</div>
  <div class="abs field" style="left:263px">New Password</div>
  <div class="abs btn-create">CREATE A WEBSHOP</div>
  <svg class="abs" style="left:332px;top:316px" width="16" height="25" viewBox="0 0 16 25"><rect x="1" y="1" width="14" height="23" rx="7" fill="none" stroke="#fff" stroke-width="1.4"/><line x1="8" y1="1" x2="8" y2="11" stroke="#fff" stroke-width="1.2"/><line x1="1" y1="11" x2="15" y2="11" stroke="#fff" stroke-width="1.2"/></svg>
</header>

<section class="services">
  <article class="card sky" style="left:56px;top:381px">
    <svg width="46" height="46" viewBox="0 0 46 46"><circle cx="23" cy="23" r="21" fill="none" stroke="#fff" stroke-width="2.6"/><path d="M18 13 L32 23 L18 33 Z" fill="#fff"/></svg>
    <h3>Get started in 5 minutes</h3>
    <p>Kom igång på 5 minuter Att starta en ebutik med Kelporia tar inte mer än 5 minuter. Skapa ett konto för att komma igång. Ingenting behöver installeras på din dator.</p>
  </article>
  <article class="card night" style="left:345px;top:381px">
    <svg width="48" height="48" viewBox="0 0 48 48"><path d="M6 4h36l4 12H2z" fill="#fff"/><rect x="6" y="18" width="36" height="26" fill="none" stroke="#fff" stroke-width="3"/><rect x="12" y="24" width="10" height="20" fill="#fff"/><circle cx="35" cy="27" r="4" fill="#fff"/><path d="M27 44c0-7 4-10 8-10s8 3 8 10z" fill="#fff"/></svg>
    <h3>Create a free online store</h3>
    <p>Skapa en gratis webbutik Kelporia är en gratis tjänst. Tjänsten har varken månadskostnader eller transaktionsavgifter på det du säljer.</p>
  </article>
  <article class="card night" style="left:56px;top:512px">
    <svg width="44" height="44" viewBox="0 0 44 44" fill="none" stroke="#fff" stroke-width="3"><rect x="3" y="3" width="38" height="38"/><rect x="11" y="11" width="20" height="20"/><rect x="17" y="17" width="16" height="16"/></svg>
    <h3>Intuitive user interface</h3>
    <p>Intuitivt användargränssnitt Det går snabb att lägga till nya produkter. Organisera produkter genom att dra och släppa</p>
  </article>
  <article class="card royal" style="left:345px;top:512px">
    <svg width="48" height="48" viewBox="0 0 48 48" fill="none" stroke="#fff" stroke-width="2.6"><circle cx="22" cy="22" r="19"/><ellipse cx="22" cy="22" rx="8" ry="19"/><line x1="3" y1="22" x2="41" y2="22"/><line x1="6" y1="12" x2="38" y2="12"/><line x1="6" y1="32" x2="30" y2="32"/><circle cx="34" cy="34" r="7" fill="#1f62b5"/><line x1="39" y1="39" x2="46" y2="46" stroke-width="3.5"/></svg>
    <h3>Search engine optimized</h3>
    <p>Sökmotoroptimerad Kelporia är genomgående skapat med sökmotoroptimering som en fokus punkt</p>
  </article>
  <article class="card sky" style="left:56px;top:643px">
    <svg width="48" height="44" viewBox="0 0 48 44"><path d="M4 2h40l3 14H1z" fill="#fff"/><path d="M8 2v14M16 2v14M24 2v14M32 2v14M40 2v14" stroke="#1e9ad6" stroke-width="2"/><rect x="5" y="18" width="38" height="24" fill="none" stroke="#fff" stroke-width="3"/><rect x="10" y="24" width="9" height="18" fill="#fff"/><rect x="26" y="25" width="11" height="8" fill="none" stroke="#fff" stroke-width="2.5"/></svg>
    <h3>Design your shop</h3>
    <p>Designa din webshop Välj bland färdiga utseende mallar eller skapa din egen grafiska profil med ett par klick.</p>
  </article>
  <article class="card night" style="left:345px;top:643px">
    <svg width="44" height="44" viewBox="0 0 44 44" fill="none" stroke="#fff" stroke-width="3"><rect x="3" y="3" width="38" height="38"/><rect x="10" y="10" width="10" height="9"/><rect x="24" y="10" width="10" height="9"/><path d="M9 34l9-7 7 4 10-9"/></svg>
    <h3>Smart dashboard</h3>
    <p>Smart Dashboard På startsidan i din webbutik får du en överblick om senast inkomna ordrar, analys och statistik om försäljningar mm.</p>
  </article>
</section>

<section class="features">
  <h2 class="features-title">Our <em>Features</em></h2>
  <div class="features-rule"></div>

  <div class="feature" style="left:56px;top:84px">
    <svg width="32" height="38" viewBox="0 0 32 38" fill="#1e9ad6"><circle cx="16" cy="9" r="7"/><path d="M4 36c0-10 5-16 12-16s12 6 12 16z"/><path d="M2 26l6 2-2 6-5-2z"/></svg>
    <h4>Technical Specifications</h4>
    <p>If you started with the free version will soon be able to upgrade to the premium version for more functionality.</p>
  </div>
  <div class="feature" style="left:251px;top:84px">
    <svg width="30" height="34" viewBox="0 0 30 34" fill="#1e9ad6"><ellipse cx="15" cy="5" rx="13" ry="4"/><path d="M2 8c0 3 6 5 13 5s13-2 13-5v6c0 3-6 5-13 5S2 17 2 14z"/><path d="M2 18c0 3 6 5 13 5s13-2 13-5v6c0 3-6 5-13 5S2 27 2 24z"/></svg>
    <h4>Unlimited Data Traffic</h4>
    <p>If you started with the free version will soon be able to upgrade to the premium version for more functionality.</p>
  </div>
  <div class="feature" style="left:446px;top:84px">
    <svg width="30" height="32" viewBox="0 0 30 32" fill="none" stroke="#1e9ad6" stroke-width="2"><path d="M15 2l12 7v14l-12 7-12-7V9z"/><circle cx="14" cy="15" r="6"/><line x1="14" y1="12" x2="14" y2="18"/><line x1="11" y1="15" x2="17" y2="15"/><line x1="18" y1="19" x2="22" y2="23" stroke-width="3"/></svg>
    <h4>Inventory Management</h4>
    <p>If you started with the free version will soon be able to upgrade to the premium version for more functionality.</p>
  </div>
  <div class="feature" style="left:56px;top:157px">
    <svg width="32" height="32" viewBox="0 0 48 48" fill="none" stroke="#1e9ad6" stroke-width="3"><circle cx="22" cy="22" r="19"/><ellipse cx="22" cy="22" rx="8" ry="19"/><line x1="3" y1="22" x2="41" y2="22"/><line x1="6" y1="12" x2="38" y2="12"/><circle cx="34" cy="34" r="7" fill="#ececec"/><line x1="39" y1="39" x2="46" y2="46" stroke-width="4"/></svg>
    <h4>Search Engine Optimized</h4>
    <p>If you started with the free version will soon be able to upgrade to the premium version for more functionality.</p>
  </div>
  <div class="feature" style="left:251px;top:157px">
    <svg width="32" height="30" viewBox="0 0 32 30" fill="none" stroke="#1e9ad6" stroke-width="2.6"><path d="M1 3h6l4 15h16l3-11H9"/><circle cx="13" cy="25" r="2.5" fill="#1e9ad6"/><circle cx="25" cy="25" r="2.5" fill="#1e9ad6"/></svg>
    <h4>Edit Shipping Types</h4>
    <p>If you started with the free version will soon be able to upgrade to the premium version for more functionality.</p>
  </div>
  <div class="feature" style="left:446px;top:157px">
    <svg width="28" height="32" viewBox="0 0 28 32"><path d="M3 1h16l7 7v23H3z" fill="none" stroke="#1e9ad6" stroke-width="1.6"/><rect x="1" y="11" width="22" height="9" fill="#1e9ad6"/><text x="12" y="18.5" font-family="Roboto,sans-serif" font-size="7" fill="#fff" text-anchor="middle">ICO</text></svg>
    <h4>FavIcon Support</h4>
    <p>If you started with the free version will soon be able to upgrade to the premium version for more functionality.</p>
  </div>
</section>

<footer class="footer">
  <div class="brand">Kelporia</div>
  <div class="contact" style="left:217px">
    <i><svg width="9" height="7" viewBox="0 0 9 7" fill="none" stroke="#fff" stroke-width="1"><rect x=".5" y=".5" width="8" height="6"/><path d="M.5 .5l4 3 4-3"/></svg></i>
    info@kelporia.example
  </div>
  <div class="contact" style="left:348px">
    <i></i>
    Kelporia on Flitter
  </div>
  <nav class="footer-nav">
    <span>Home</span><span class="sep">|</span>
    <span>Services</span><span class="sep">|</span>
    <span>About us</span><span class="sep">|</span>
    <span>Our stores</span><span class="sep">|</span>
    <span>Features</span><span class="sep">|</span>
    <span>Contact</span>
  </nav>
  <div class="footer-line"></div>
  <div class="copyright">© 2016 Kelporia. All Rights Reserved</div>
  <div class="social"><span></span><span></span><span></span><span></span><span></span></div>
</footer>

</body>
</html>
```